Business Cards and Stationary
Silver Pine
Professional
Tom Feaster, P.G.
Founder
4718 Wexley Lane
Maple Falls, Colorado 80777
tfeaster@silverpinenviroq.com
www.silverpinenviroq.com
Consulting Compliance Training

```html
<!DOCTYPE html>
<html lang="en">
<head>
<meta charset="utf-8">
<title>Silver Pine Stationery Set</title>
<link rel="stylesheet" href="https://fonts.googleapis.com/css2?family=Tinos:wght@400;700&display=swap">
<style>
  :root {
    --frame: #d9d9d9;
    --paper: #ffffff;
    --edge: #c9c9c9;
    --brand-red: #b3191c;
    --band-dark: #6e2612;
    --band-light: #c9714a;
    --ink: #222222;
    --flap-line: #dcdcdc;
  }
  * { margin: 0; padding: 0; box-sizing: border-box; }
  html, body { width: 1200px; height: 919px; overflow: hidden; background: var(--frame); }
  body { position: relative; font-family: "Tinos", "Times New Roman", serif; color: var(--ink); }

  .board { position: absolute; left: 12px; top: 12px; width: 1176px; height: 895px; background: var(--paper); }

  .sheet { position: absolute; background: var(--paper); border: 1px solid var(--edge); box-shadow: 2px 3px 6px rgba(0,0,0,.12); }

  .brand-name { font-weight: 700; color: var(--brand-red); text-transform: uppercase; letter-spacing: .02em; line-height: 1; white-space: nowrap; vertical-align: middle; }
  .brand-mark { display: inline-block; border-radius: 50%; background: var(--brand-red); vertical-align: middle; }

  .band { position: absolute; height: 4px;
    background: linear-gradient(90deg, rgba(201,113,74,0) 0%, var(--band-light) 12%, var(--band-dark) 50%, var(--band-light) 88%, rgba(201,113,74,0) 100%); }
  .band--fade-right { background: linear-gradient(90deg, var(--band-dark) 0%, var(--band-light) 45%, rgba(201,113,74,0) 100%); }

  /* Letterhead */
  .letterhead { left: 388px; top: 63px; width: 520px; height: 805px; }
  .letterhead .brand { position: absolute; left: 0; right: 0; top: 78px; text-align: center; }
  .letterhead .brand-name { font-size: 20px; }
  .letterhead .brand-mark { width: 12px; height: 12px; margin-right: 7px; }
  .letterhead .band { left: 0; right: 0; top: 104px; }
  .letterhead .contact { position: absolute; left: 0; right: 0; top: 114px; text-align: center; font-size: 8.5px; white-space: nowrap; }

  /* Envelope */
  .envelope { left: 43px; top: 280px; width: 695px; height: 363px; }
  .envelope .flap { position: absolute; inset: 0; }
  .envelope .brand { position: absolute; left: 28px; top: 180px; }
  .envelope .brand-name { font-size: 20px; }
  .envelope .brand-mark { width: 12px; height: 12px; margin-right: 7px; }
  .envelope .band { left: 0; width: 300px; top: 206px; }
  .envelope .return-address { position: absolute; left: 30px; top: 228px; font-size: 9px; white-space: nowrap; }

  /* Business card */
  .business-card { left: 858px; top: 358px; width: 272px; height: 97px; }
  .business-card .brand { position: absolute; left: 0; right: 0; top: 12px; text-align: center; }
  .business-card .brand-name { font-size: 11px; }
  .business-card .brand-mark { width: 7px; height: 7px; margin-right: 4px; }
  .business-card .band { left: 0; right: 0; top: 30px; height: 3px; }
  .business-card .person { position: absolute; left: 0; right: 0; top: 52px; text-align: center; line-height: 1.1; }
  .business-card .person-name { font-size: 7px; }
  .business-card .person-title { font-size: 5px; margin-top: 1px; }
  .business-card .card-contact { position: absolute; left: 0; right: 0; top: 78px; text-align: center; font-size: 4px; line-height: 1.5; white-space: nowrap; }
</style>
</head>
<body>
  <main class="board">

    <section class="sheet letterhead" aria-label="Letterhead">
      <div class="brand"><span class="brand-mark"></span><span class="brand-name">Silver Pine</span></div>
      <div class="band"></div>
      <p class="contact">4718 Wexley Lane, Maple Falls, Colorado 80777 &nbsp;&nbsp; Phone: 303-555-0147 | www.silverpinenviroq.com</p>
    </section>

    <section class="sheet envelope" aria-label="Envelope">
      <svg class="flap" width="695" height="363" viewBox="0 0 695 363" aria-hidden="true">
        <path d="M0 0 L290 95 Q347 115 404 95 L695 0" fill="none" stroke="var(--flap-line)" stroke-width="1.5"/>
      </svg>
      <div class="brand"><span class="brand-mark"></span><span class="brand-name">Silver Pine</span></div>
      <div class="band band--fade-right"></div>
      <p class="return-address">4718 Wexley Lane, Maple Falls, Colorado 80777</p>
    </section>

    <section class="sheet business-card" aria-label="Business card">
      <div class="brand"><span class="brand-mark"></span><span class="brand-name">Silver Pine</span></div>
      <div class="band"></div>
      <div class="person">
        <p class="person-name">Tom Feaster, P.G.</p>
        <p class="person-title">Founder</p>
      </div>
      <div class="card-contact">
        <p>4718 Wexley Lane, Maple Falls, Colorado 80777</p>
        <p>Phone: 303-555-0147 | Email: tfeaster@silverpinenviroq.com | www.silverpinenviroq.com</p>
      </div>
    </section>

  </main>
</body>
</html>
```